Visitenkarten-Design für Immobilienunternehmen
Zielgruppe
Wir sind ein Immobilienunternehmen mit 2 Büros - alle Zielgruppen, jung und alt, arm und reich, Käufer und Verkäufer, privat und gewerblich suchen ein neues hochwertiges Design für die Visitenkarte
Aufgabenstellung
seriös, nicht angestaubt, Firmenfarben (rot,blau, weiß, siehe Bilder)
2-seitg bedruckt (allgemein auf der einen Seite, personenvorstellung mit bild auf der anderen seite)
Ein Visitenkartendesign für 2 Personen

```html
<!DOCTYPE html>
<html lang="de">
<head>
<meta charset="utf-8">
<title>Visitenkarte – Marlene Hofbauer</title>
<link href="https://fonts.googleapis.com/css2?family=Raleway:wght@400;700;900&display=swap" rel="stylesheet">
<style>
  :root {
    --brand-blue: #0f2a8a;
    --brand-red: #e8140c;
    --frame-mid: #4a1f6a;
    --paper: #ffffff;
    --photo-green: #8fb34a;
    --photo-dark: #33402a;
  }
  html, body {
    margin: 0;
    padding: 0;
    width: 1200px;
    height: 776px;
    overflow: hidden;
    background: var(--paper);
  }
  .card {
    position: relative;
    width: 1200px;
    height: 776px;
    background: linear-gradient(90deg, var(--brand-blue) 0%, var(--frame-mid) 50%, var(--brand-red) 100%);
    font-family: "Raleway", sans-serif;
    color: var(--brand-blue);
  }
  .card__inner {
    position: absolute;
    inset: 17px;
    background: var(--paper);
  }
  .portrait {
    position: absolute;
    left: 66px;
    top: 66px;
    width: 392px;
    height: 392px;
  }
  .contact-name {
    position: absolute;
    left: 537px;
    top: 80px;
    margin: 0;
    font-size: 60px;
    line-height: 1;
    font-weight: 900;
    letter-spacing: -0.5px;
    white-space: nowrap;
  }
  .contact-role {
    position: absolute;
    left: 538px;
    margin: 0;
    font-size: 42px;
    line-height: 1;
    font-weight: 400;
    white-space: nowrap;
  }
  .contact-role--office { top: 170px; }
  .contact-role--advisor { top: 224px; }
  .contact-phone {
    position: absolute;
    left: 538px;
    top: 362px;
    margin: 0;
    font-size: 58px;
    line-height: 1;
    font-weight: 700;
    color: var(--brand-red);
    font-variant-numeric: oldstyle-nums;
    white-space: nowrap;
  }
  .referral-note {
    position: absolute;
    left: 71px;
    top: 556px;
    width: 1010px;
    margin: 0;
    font-size: 44px;
    line-height: 54px;
    font-weight: 400;
  }
</style>
</head>
<body>
  <div class="card">
    <div class="card__inner">
      <svg class="portrait" viewBox="0 0 392 392" role="img" aria-label="Porträtfoto der Immobilienberaterin im blauen Blazer vor grünem Hintergrund">
        <defs>
          <linearGradient id="portrait-fill" x1="0" y1="0" x2="1" y2="1">
            <stop offset="0" stop-color="var(--photo-dark)"/>
            <stop offset="0.55" stop-color="var(--photo-green)"/>
            <stop offset="1" stop-color="#2a4aa8"/>
          </linearGradient>
        </defs>
        <circle cx="196" cy="196" r="185" fill="url(#portrait-fill)"/>
        <circle cx="196" cy="196" r="190" fill="none" stroke="var(--brand-blue)" stroke-width="11"/>
      </svg>

      <h1 class="contact-name">Marlene Hofbauer</h1>
      <p class="contact-role contact-role--office">Büromanagement</p>
      <p class="contact-role contact-role--advisor">Immobilienberaterin</p>
      <p class="contact-phone">0151/4729386</p>

      <p class="referral-note">Kennen Sie jemanden, der ein Haus oder eine Wohnung kaufen oder verkaufen möchte? Bitte rufen Sie mich an. Ich freue mich!</p>
    </div>
  </div>
</body>
</html>
```